Roadside building business signage for a holistic health clinic.

Replace signs as shown in the attached file. They are perforated stickers that go on the windows as shown. Looking for something that has our logo and says the name of the practice with logo (Fernbrook Health & Wellness) also boldly says Acupuncture, IV Vitamins, and Holistic Health.
Possibly our phone number as well 318-627-5194
Updates

Please don't use pink except the logo. Earthy, organic tone colors appreciated.

Need of eye catching window signage of a holistic clinic on a brick building. Pink, purple, sage green, white color. Logo is pink on a white background. Please don't overload with too much pink. Words to include are "Fernbrook Health and Wellness(name of business)", "Direct Primary Care", " Medical acupuncture", "IV Vitamin Therapy", "fernbrookcare-example.com","318-627-5194".

Target Market(s)

People will see in their cars passing by the building. Busy roadside so need to be visible while passing in fast speed.

Industry/Entity Type

Health & Wellness

Font styles to use
Sans Serif

Colors

Designer to choose colors to be used in the design.

Requirements
Must have
• On sign must have words Holistic Medicine, Medical Acupuncture, Direct Primary Care and IV vitamins.
Nice to have
• Simple, minimalistic, artistic yet has clear message. White, Black, Violet, Pink (logo), Dark green, Sage green.
Should not have
• Bold colors (red, yellow, blue), same tone colors. Blue waves on the current signage (uploaded file) must go.

```html
<!DOCTYPE html>
<html lang="en">
<head>
<meta charset="utf-8">
<title>Fernbrook Health &amp; Wellness – Window Sign</title>
<link href="https://fonts.googleapis.com/css2?family=Rubik:wght@400;500;600&display=swap" rel="stylesheet">
<style>
  :root {
    --backdrop: #156663;
    --forest: #0d4a3b;
    --sage: #8fa888;
    --sage-deep: #6f8c6a;
    --sage-mist: #e4ecdf;
    --violet: #6b4f8a;
    --lavender: #ece6f2;
    --white: #ffffff;
    --logo-pink: #e0488c;
  }
  * { margin: 0; padding: 0; box-sizing: border-box; }
  html, body {
    width: 1200px;
    height: 2280px;
    overflow: hidden;
    background: var(--backdrop);
  }
  .canvas {
    position: relative;
    width: 1200px;
    height: 2280px;
    background: var(--backdrop);
  }
  .window-sign {
    position: absolute;
    left: 96px;
    top: 636px;
    width: 1008px;
    height: 1008px;
    background: var(--white);
    box-shadow: 0 20px 60px rgba(0, 0, 0, 0.28);
    overflow: hidden;
    font-family: "Rubik", sans-serif;
  }
  .sign-art {
    position: absolute;
    left: 0;
    top: 0;
    width: 1008px;
    height: 540px;
  }
  .headline {
    position: absolute;
    left: 0;
    top: 42px;
    width: 100%;
    text-align: center;
    font-weight: 600;
    font-size: 104px;
    line-height: 1;
    letter-spacing: -0.01em;
    color: var(--white);
  }
  .brand {
    position: absolute;
    left: 0;
    top: 238px;
    width: 100%;
    text-align: center;
    color: var(--forest);
  }
  .brand-mark {
    width: 110px;
    height: 110px;
    margin: 0 auto 22px;
    border-radius: 50%;
    background: var(--logo-pink);
  }
  .brand-name {
    font-weight: 500;
    font-size: 84px;
    letter-spacing: 0.12em;
    line-height: 1;
    padding-left: 0.12em;
  }
  .brand-tagline {
    margin-top: 14px;
    font-weight: 500;
    font-size: 28px;
    letter-spacing: 0.36em;
    line-height: 1;
    padding-left: 0.36em;
    color: var(--violet);
  }
  .services-band {
    position: absolute;
    left: 0;
    top: 540px;
    width: 100%;
    height: 300px;
    background: var(--forest);
    display: flex;
    flex-direction: column;
    align-items: center;
    justify-content: center;
    list-style: none;
    color: var(--white);
    font-weight: 500;
    font-size: 52px;
    line-height: 1.3;
  }
  .contact-row {
    position: absolute;
    left: 0;
    top: 840px;
    width: 100%;
    height: 168px;
    display: flex;
    align-items: center;
    justify-content: center;
  }
  .contact-rule {
    flex: 1;
    height: 3px;
    background: var(--violet);
  }
  .contact-details {
    padding: 0 40px;
    text-align: center;
    color: var(--forest);
  }
  .phone {
    display: flex;
    align-items: center;
    justify-content: center;
    gap: 26px;
    font-weight: 500;
    font-size: 70px;
    letter-spacing: -0.02em;
    line-height: 1;
  }
  .phone-icon { width: 46px; height: 46px; }
  .website {
    margin-top: 12px;
    font-weight: 400;
    font-size: 32px;
    line-height: 1;
    color: var(--violet);
  }
</style>
</head>
<body>
<main class="canvas">
  <section class="window-sign">
    <svg class="sign-art" viewBox="0 0 1008 540" aria-hidden="true">
      <defs>
        <linearGradient id="headerFill" x1="0" y1="0" x2="1" y2="0">
          <stop offset="0" stop-color="#9cb495"/>
          <stop offset="1" stop-color="#6f8c6a"/>
        </linearGradient>
      </defs>
      <path d="M0 150 C 300 210, 650 250, 1008 240 L1008 470 C 700 380, 300 300, 0 280 Z" fill="#e4ecdf" opacity="0.8"/>
      <path d="M0 190 C 320 250, 680 280, 1008 280 L1008 380 C 700 320, 330 260, 0 240 Z" fill="#ece6f2" opacity="0.9"/>
      <path d="M0 0 H1008 V210 C 680 240, 330 200, 0 170 Z" fill="url(#headerFill)"/>
      <path d="M0 170 C 330 200, 680 240, 1008 210" fill="none" stroke="#6b4f8a" stroke-width="4" opacity="0.6"/>
    </svg>

    <h1 class="headline">Practice with</h1>

    <div class="brand">
      <div class="brand-mark"></div>
      <div class="brand-name">FERNBROOK</div>
      <div class="brand-tagline">HEALTH &amp; WELLNESS</div>
    </div>

    <ul class="services-band">
      <li>Direct Primary Care</li>
      <li>Medical Acupuncture</li>
      <li>IV Vitamin Therapy</li>
      <li>Holistic Medicine</li>
    </ul>

    <div class="contact-row">
      <span class="contact-rule"></span>
      <div class="contact-details">
        <div class="phone">
          <svg class="phone-icon" viewBox="0 0 50 50" aria-hidden="true">
            <circle cx="25" cy="25" r="25" fill="#0d4a3b"/>
            <path d="M17 13 l5 -1 l3 7 l-3 3 c2 4 4 6 8 8 l3 -3 l7 3 l-1 5 c-1 2 -3 3 -5 3 c-10 -1 -19 -10 -20 -20 c0 -2 1 -4 3 -5 z" fill="#ffffff"/>
          </svg>
          318-627-5194
        </div>
        <div class="website">fernbrookcare-example.com</div>
      </div>
      <span class="contact-rule"></span>
    </div>
  </section>
</main>
</body>
</html>
```